valtheon construction

i want a construction website something that really epic and eye catchy

we do full Renovation Restoration Construction

if anyone can make my jaw drop there well be a big Reward ,

i have attach my logo

Industry/Entity Type

Construction

Number of Pages Required

4 page

```html
<!DOCTYPE html>
<html lang="en">
<head>
<meta charset="utf-8">
<title>Valtheon Construction</title>
<link rel="stylesheet" href="https://fonts.googleapis.com/css2?family=Open+Sans:wght@400;600;700&family=Roboto:wght@300;400;500;700&display=swap">
<style>
:root{
  --red:#a30d0d;
  --red-dark:#7e0808;
  --ink:#333333;
  --muted:#777777;
  --grey-band:#efefef;
  --white:#ffffff;
  --footer:#2b2b2b;
  --footer-bottom:#1e1e1e;
  --footer-text:#bbbbbb;
}
*{box-sizing:border-box;margin:0;padding:0}
html,body{width:1200px;height:3820px;overflow:hidden}
body{font-family:"Open Sans",Arial,sans-serif;color:var(--ink);background:var(--white);position:relative}
h1,h2,h3{font-family:"Roboto",Arial,sans-serif;font-weight:400}
.section-title{color:var(--red);font-size:40px;text-align:center}
.intro{font-size:14px;color:var(--muted);text-align:center;line-height:22px;width:560px;margin:14px auto 0}
.btn{display:inline-block;font-family:"Roboto",Arial,sans-serif;font-size:15px;padding:10px 22px;border:2px solid var(--red);text-transform:uppercase}
.btn-solid{background:var(--red);color:var(--white)}
.btn-ghost{background:var(--white);color:var(--red)}
.photo{display:block}

/* header + hero */
.hero{position:absolute;top:0;left:0;width:1200px;height:660px;overflow:hidden}
.hero-photo{position:absolute;inset:0;background:linear-gradient(180deg,#c9cdd0 0%,#eef0f1 18%,#fbfbfb 40%,#f2f2f2 62%,#b9b9b9 80%,#8d8d8d 100%)}
.site-header{position:absolute;top:0;left:0;width:1200px;height:110px}
.brand{position:absolute;left:80px;top:0;width:290px;height:104px;background:var(--white);display:flex;align-items:center;gap:12px;padding:0 22px;box-shadow:0 3px 8px rgba(0,0,0,.2)}
.brand-mark{width:40px;height:40px;background:var(--red);flex:none}
.brand-name{font-family:"Roboto",Arial,sans-serif;font-size:20px;font-weight:700;color:var(--red);line-height:22px;text-transform:uppercase}
.nav{position:absolute;right:72px;top:30px;display:flex;gap:4px;background:var(--white);padding:6px;box-shadow:0 2px 6px rgba(0,0,0,.12)}
.nav a{font-family:"Roboto",Arial,sans-serif;font-size:14px;color:#444;padding:8px 12px;text-decoration:none}
.nav a.active{border:1px solid var(--red);color:var(--red)}
.hero-title{position:absolute;left:108px;top:250px;width:600px;font-size:44px;line-height:50px;font-weight:500;color:var(--red);text-shadow:0 1px 2px rgba(255,255,255,.8)}
.hero-actions{position:absolute;left:108px;top:390px;display:flex;gap:30px}

/* contact band */
.contact-band{position:absolute;top:660px;left:0;width:1200px;height:180px;background:linear-gradient(180deg,var(--red) 0%,var(--red-dark) 100%)}
.contact-band h2{color:var(--white);font-size:34px;text-align:center;padding-top:30px}
.contact-form{display:flex;justify-content:center;gap:14px;margin-top:24px}
.field{width:210px;height:34px;border:1px solid rgba(255,255,255,.6);color:var(--white);font-size:13px;padding:8px 10px}
.subscribe{height:34px;padding:5px 18px;border:2px solid var(--white);color:var(--white);font-size:16px}

/* benefits */
.benefits{position:absolute;top:840px;left:0;width:1200px;height:480px;text-align:center}
.benefits .section-title{margin-top:26px}
.benefit-row{display:flex;justify-content:center;gap:72px;margin-top:30px}
.benefit{width:310px}
.benefit .photo{width:310px;height:172px;box-shadow:0 2px 6px rgba(0,0,0,.15)}
.benefit h3{color:var(--red);font-size:19px;font-weight:500;margin-top:18px}
.benefit p{font-size:12px;color:var(--muted);line-height:19px;margin-top:8px;padding:0 20px}

/* dream design */
.dream{position:absolute;top:1320px;left:0;width:1200px;height:340px;background:var(--grey-band)}
.dream .photo{position:absolute;left:60px;top:50px;width:520px;height:230px;background:linear-gradient(180deg,#eef0f2 0%,#d3d8dc 35%,#9aa3aa 60%,#4a5157 80%,#2c3035 100%);clip-path:polygon(12% 18%,70% 4%,96% 30%,100% 82%,60% 100%,0 86%)}
.dream-copy{position:absolute;left:640px;top:56px}
.dream-copy h2{font-size:40px;color:var(--red)}
.check-list{list-style:none;margin-top:16px}
.check-list li{display:flex;align-items:center;gap:14px;font-size:14px;color:#555;height:28px}

/* best construction */
.best{position:absolute;top:1660px;left:0;width:1200px;height:320px}
.best .section-title{margin-top:36px}
.best .photo{position:absolute;left:0;top:110px;width:1200px;height:210px;background:linear-gradient(180deg,#ffffff 0%,#dcdcdc 30%,#b4b4b4 55%,#d6d6d6 80%,#f3f3f3 100%)}

/* restoration */
.restoration{position:absolute;top:1980px;left:0;width:1200px;height:300px;background:var(--grey-band)}
.restoration-copy{position:absolute;left:80px;top:62px;width:430px;text-align:center}
.restoration-copy h2{font-size:40px;color:var(--red);white-space:nowrap}
.restoration-copy p{font-size:14px;color:#555;line-height:24px;margin-top:10px}
.restoration-copy .btn{margin-top:14px;padding:6px 18px}
.restoration .photo{position:absolute;left:680px;top:30px;width:380px;height:250px;background:linear-gradient(160deg,#ffffff 0%,#e2e2e2 35%,#9a9a9a 60%,#4e4e4e 85%,#bdbdbd 100%);clip-path:polygon(6% 22%,62% 0,100% 18%,100% 88%,46% 100%,0 82%)}

/* projects */
.projects{position:absolute;top:2280px;left:0;width:1200px;height:1000px}
.projects .section-title{margin-top:20px}
.project-grid{position:absolute;left:72px;top:168px;width:1056px;height:800px;display:grid;grid-template-columns:repeat(4,1fr);grid-template-rows:repeat(6,1fr);gap:8px}
.project-label{background:#2a2a2a;color:var(--white);display:flex;flex-direction:column;align-items:center;justify-content:center;font-size:14px}
.project-label span{font-size:11px;color:#aaa;margin-top:6px}

/* closing */
.closing{position:absolute;top:3300px;left:0;width:1200px;height:230px;text-align:center}
.closing h2{font-size:36px;color:var(--ink)}
.closing .btn{margin-top:20px;padding:6px 20px}

/* footer */
.site-footer{position:absolute;top:3540px;left:0;width:1200px;height:230px;background:var(--footer);color:var(--footer-text);display:flex;padding:26px 40px 0}
.footer-col{width:280px;font-size:12px;line-height:20px}
.footer-col h4{font-family:"Roboto",Arial,sans-serif;color:var(--white);font-size:14px;font-weight:500;margin-bottom:12px}
.footer-col ul{list-style:none}
.feed-item{display:flex;gap:10px;margin-bottom:12px;padding-right:20px}
.feed-thumb{width:40px;height:40px;background:#555;flex:none}
.feed-item small{display:block;color:#888;font-size:11px}
.tweet-dot{width:18px;height:18px;border-radius:50%;background:#888;flex:none;margin-top:2px}
.contact-line{display:flex;gap:10px;align-items:center;margin-bottom:8px}
.socials{display:flex;gap:14px;margin-top:10px}
.socials span{width:14px;height:14px;border-radius:50%;background:#999}
.footer-bottom{position:absolute;top:3770px;left:0;width:1200px;height:50px;background:var(--footer-bottom);color:#999;font-size:12px;text-align:center;line-height:50px}
.footer-bottom b{color:var(--red);font-weight:400}
.to-top{position:absolute;right:16px;top:3780px;width:30px;height:30px;border-radius:50%;background:#555}
</style>
</head>
<body>

<section class="hero">
  <div class="hero-photo photo" role="img" aria-label="Bright white modern living room with sofas, dining table and potted plants"></div>
  <header class="site-header">
    <div class="brand"><span class="brand-mark"></span><span class="brand-name">Valtheon<br>Construction</span></div>
    <nav class="nav">
      <a class="active">HOME</a><a>ABOUT</a><a>MANAGEMENT</a><a>PROJECT</a><a>CLIENT</a><a>CONTACT</a>
    </nav>
  </header>
  <h1 class="hero-title">We are a Creative Renovation &amp; Restortion Design Studio</h1>
  <div class="hero-actions">
    <span class="btn btn-solid">Get Started</span>
    <span class="btn btn-ghost">Sample Project</span>
  </div>
</section>

<section class="contact-band">
  <h2>Interested Get in Touch With Us</h2>
  <div class="contact-form">
    <span class="field">Name</span>
    <span class="field">Company Name</span>
    <span class="field">E-Mail</span>
    <span class="subscribe">Subscribe</span>
  </div>
</section>

<section class="benefits">
  <h2 class="section-title">Benefits</h2>
  <p class="intro">Lorem Ipsum is simply dummy text of the printing and typesetting industry. Lorem Ipsum has been the industry's standard dummy text ever since the 1500s.</p>
  <div class="benefit-row">
    <div class="benefit">
      <div class="photo" role="img" aria-label="Modern interior lounge with dark wooden furniture" style="background:linear-gradient(180deg,#e9e4dc 0%,#c4b8a8 40%,#6b5a4a 75%,#3e3229 100%)"></div>
      <h3>Lorem Ipsum is a dummy</h3>
      <p>Lorem Ipsum is simply dummy text of the printing and typesetting industry.</p>
    </div>
    <div class="benefit">
      <div class="photo" role="img" aria-label="Yellow safety helmet resting on construction plans" style="background:linear-gradient(180deg,#f7f7f2 0%,#f2d21c 35%,#e0b800 60%,#d8dde2 100%)"></div>
      <h3>Lorem Ipsum is a dummy</h3>
      <p>Lorem Ipsum is simply dummy text of the printing and typesetting industry.</p>
    </div>
    <div class="benefit">
      <div class="photo" role="img" aria-label="Builder in red overalls with tools on a white background" style="background:linear-gradient(180deg,#fafafa 0%,#e23a32 35%,#b81d18 65%,#f2f2f2 100%)"></div>
      <h3>100% Money Back Guarantee</h3>
      <p>Lorem Ipsum is simply dummy text of the printing and typesetting industry.</p>
    </div>
  </div>
</section>

<section class="dream">
  <div class="photo" role="img" aria-label="Contemporary white multi-level villa with curved cantilevered floors"></div>
  <div class="dream-copy">
    <h2>Dream Design</h2>
    <ul class="check-list">
      <li><svg width="14" height="14" viewBox="0 0 14 14"><path d="M2 7l3 3 7-7" fill="none" stroke="#555" stroke-width="2"/></svg>Affordable at Your Rate</li>
      <li><svg width="14" height="14" viewBox="0 0 14 14"><path d="M2 7l3 3 7-7" fill="none" stroke="#555" stroke-width="2"/></svg>Fast Timeframe set by You</li>
      <li><svg width="14" height="14" viewBox="0 0 14 14"><path d="M2 7l3 3 7-7" fill="none" stroke="#555" stroke-width="2"/></svg>Expert Designers</li>
      <li><svg width="14" height="14" viewBox="0 0 14 14"><path d="M2 7l3 3 7-7" fill="none" stroke="#555" stroke-width="2"/></svg>5-20 Concepts</li>
      <li><svg width="14" height="14" viewBox="0 0 14 14"><path d="M2 7l3 3 7-7" fill="none" stroke="#555" stroke-width="2"/></svg>100% Money Back Guarantee</li>
    </ul>
  </div>
</section>

<section class="best">
  <h2 class="section-title">Best Construction</h2>
  <div class="photo" role="img" aria-label="Pencil sketch of a modern house with trees across the full width"></div>
</section>

<section class="restoration">
  <div class="restoration-copy">
    <h2>Realise Restoration</h2>
    <p>Access to Project management Tools to<br>Get your Project Underway</p>
    <span class="btn btn-solid">Get Started</span>
  </div>
  <div class="photo" role="img" aria-label="White modern cube house with large glass windows"></div>
</section>

<section class="projects">
  <h2 class="section-title">Our Projects</h2>
  <p class="intro">Lorem Ipsum is simply dummy text of the printing and typesetting industry. Lorem Ipsum has been the industry's standard dummy text ever since the 1500s.</p>
  <div class="project-grid">
    <div class="photo" style="grid-column:1;grid-row:1/4;background:linear-gradient(180deg,#2e2e2e 0%,#8a8a8a 30%,#e6e6e6 60%,#bdbdbd 100%)" role="img" aria-label="White dining room with chandelier"></div>
    <div class="project-label" style="grid-column:2;grid-row:1/3">Villa in Vegas<span>view →</span></div>
    <div class="photo" style="grid-column:3;grid-row:1/3;background:linear-gradient(180deg,#f4efe4 0%,#d9ceb8 45%,#8d7e66 75%,#5e5240 100%)" role="img" aria-label="Bright living room with shelving"></div>
    <div class="photo" style="grid-column:4;grid-row:1/4;background:linear-gradient(180deg,#3f64c8 0%,#6d8ee0 30%,#f0a53a 55%,#c86a1e 68%,#1c2a6e 100%)" role="img" aria-label="Triangular glass house lit at dusk beside water"></div>
    <div class="photo" style="grid-column:2;grid-row:3/5;background:linear-gradient(180deg,#1f2a33 0%,#52606c 40%,#c5d2da 75%,#e8eef2 100%)" role="img" aria-label="Modern atrium with open staircase"></div>
    <div class="photo" style="grid-column:3;grid-row:3/5;background:linear-gradient(180deg,#e6e6e6 0%,#b5ada2 45%,#5e554a 80%,#3a332b 100%)" role="img" aria-label="Lounge with sofas and large windows"></div>
    <div class="photo" style="grid-column:1;grid-row:4/6;background:linear-gradient(180deg,#f7f7f7 0%,#dcdcdc 50%,#7a7a7a 85%,#4a4a4a 100%)" role="img" aria-label="White open plan living area"></div>
    <div class="photo" style="grid-column:4;grid-row:4/6;background:linear-gradient(180deg,#161616 0%,#3a3a3a 30%,#d8dde0 50%,#2a2a2a 75%,#111 100%)" role="img" aria-label="Home cinema room with dark walls"></div>
    <div class="photo" style="grid-column:2;grid-row:5/7;background:linear-gradient(180deg,#2a241d 0%,#7a6650 40%,#c9b596 75%,#e9dfcc 100%)" role="img" aria-label="Terrace with wooden deck and lounge chairs"></div>
    <div class="photo" style="grid-column:3;grid-row:5/7;background:linear-gradient(180deg,#fbfbfb 0%,#e2e2e2 45%,#8e8e8e 80%,#5c5c5c 100%)" role="img" aria-label="Minimal white lounge with grey armchairs"></div>
    <div class="photo" style="grid-column:1;grid-row:6;background:linear-gradient(180deg,#ece6dc 0%,#a49a8c 55%,#4e463e 100%)" role="img" aria-label="Kitchen with island counter"></div>
    <div class="photo" style="grid-column:4;grid-row:6;background:linear-gradient(180deg,#f2f2f2 0%,#c6c6c6 55%,#7c7c7c 100%)" role="img" aria-label="Bright sitting room with lamps"></div>
  </div>
</section>

<section class="closing">
  <h2>Best Valtheon Construction</h2>
  <p class="intro">Lorem Ipsum is simply dummy text of the printing and typesetting industry. Lorem Ipsum has been the industry's standard dummy text ever since the 1500s.</p>
  <span class="btn btn-solid">Get Started</span>
</section>

<footer class="site-footer">
  <div class="footer-col">
    <h4>Links</h4>
    <ul><li>Home</li><li>Privacy Policy</li><li>Terms &amp; Conditions</li><li>FAQs</li></ul>
  </div>
  <div class="footer-col">
    <h4>News Feed</h4>
    <div class="feed-item"><span class="feed-thumb"></span><div>Clara Denholm posted a new blog<small>Today 3:00 pm - 12.06.2015</small></div></div>
    <div class="feed-item"><span class="feed-thumb"></span><div>Owen Partridge posted a message on Ruth Calloway's wall<small>Today 3:00 pm - 12.06.2015</small></div></div>
  </div>
  <div class="footer-col">
    <h4>Recent Tweets</h4>
    <div class="feed-item"><span class="tweet-dot"></span><div>@buildnotes new site plans are live<small>4 days ago</small></div></div>
    <div class="feed-item"><span class="tweet-dot"></span><div>@buildnotes thanks for the kind words<small>4 days ago</small></div></div>
  </div>
  <div class="footer-col">
    <h4>Social Links</h4>
    <div class="contact-line"><svg width="12" height="14" viewBox="0 0 12 14"><path d="M6 13C2 8 1 6 1 5a5 5 0 0110 0c0 1-1 3-5 8z" fill="#999"/><circle cx="6" cy="5" r="1.8" fill="#2b2b2b"/></svg>Lorem Ipsum is simply dummy text of the print</div>
    <div class="contact-line"><svg width="12" height="12" viewBox="0 0 12 12"><path d="M2 1h3l1 3-2 1a7 7 0 003 3l1-2 3 1v3c-6 0-10-4-10-9z" fill="#999"/></svg>123 456 7890</div>
    <div class="contact-line"><svg width="14" height="10" viewBox="0 0 14 10"><rect x="0.5" y="0.5" width="13" height="9" fill="none" stroke="#999"/><path d="M1 1l6 5 6-5" fill="none" stroke="#999"/></svg>info@valtheon.com</div>
    <div class="socials"><span></span><span></span><span></span><span></span><span></span><span></span></div>
  </div>
</footer>
<div class="footer-bottom">© <b>Valtheon</b> 2015 , All Rights Reserved.</div>
<div class="to-top"></div>

</body>
</html>
```